Ashford Plains deaerator 25 Year

Reason: need individual names on business cards. Also need higher resolution.

Industry/Entity Type

Business

Contact Information for Business Card

See sample business card

```html
<!DOCTYPE html>
<html lang="en">
<head>
<meta charset="utf-8">
<title>Ashford Plains deaerator – Business Cards</title>
<link rel="stylesheet" href="https://fonts.googleapis.com/css2?family=Oswald:wght@300;400;500;600&display=swap">
<style>
  :root {
    --backdrop: #1e1e1e;
    --card-dark: #151515;
    --card-light: #f7f7f5;
    --silver: #c9c9c9;
    --ink: #1a1a1a;
    --ink-soft: #3a3a3a;
    --mark-grey: #6e6e6e;
    --accent-red: #d0262b;
  }
  * { margin: 0; padding: 0; box-sizing: border-box; }
  html, body {
    width: 1200px; height: 1200px; overflow: hidden;
    background: var(--backdrop);
    font-family: "Oswald", sans-serif;
  }
  .canvas { position: relative; width: 1200px; height: 1200px; }

  .card {
    position: absolute;
    left: 323px;
    width: 556px;
    height: 346px;
  }

  /* Front side */
  .card--front {
    top: 202px;
    background: var(--card-dark);
    display: flex;
    flex-direction: column;
    align-items: center;
    padding-top: 54px;
  }
  .card--front .brand-dot {
    width: 96px; height: 96px;
    border-radius: 50%;
    background: var(--silver);
  }
  .card--front .brand-name {
    margin-top: 26px;
    font-size: 30px;
    font-weight: 400;
    color: var(--silver);
    letter-spacing: 0.5px;
    line-height: 1;
  }
  .card--front .brand-rule {
    margin-top: 12px;
    width: 300px;
    height: 1px;
    background: var(--silver);
  }

  /* Back side */
  .card--back {
    top: 671px;
    background: var(--card-light);
  }
  .card--back .brand-row {
    position: absolute;
    left: 0; right: 0; top: 48px;
    display: flex;
    align-items: center;
    justify-content: center;
    gap: 16px;
  }
  .card--back .brand-dot {
    width: 80px; height: 80px;
    border-radius: 50%;
    background: var(--mark-grey);
  }
  .card--back .brand-name {
    font-size: 26px;
    font-weight: 400;
    color: var(--mark-grey);
    letter-spacing: 0.5px;
  }
  .person {
    position: absolute;
    left: 0; right: 0; top: 178px;
    text-align: center;
  }
  .person__name {
    font-size: 20px;
    font-weight: 600;
    color: var(--ink);
    letter-spacing: 0.3px;
    line-height: 1.2;
  }
  .person__title {
    margin-top: 6px;
    font-size: 16px;
    font-weight: 400;
    color: var(--ink-soft);
    letter-spacing: 2px;
    line-height: 1.2;
  }
  .divider {
    position: absolute;
    left: 29px; right: 30px; top: 251px;
    height: 2px;
    background: var(--accent-red);
  }
  .contact {
    position: absolute;
    top: 274px;
    font-size: 12.5px;
    font-weight: 300;
    color: var(--ink);
    line-height: 22px;
  }
  .contact--address { left: 29px; }
  .contact--phone { left: 218px; }
  .contact--online { left: 350px; }
  .contact b { font-weight: 600; display: inline-block; width: 18px; }
</style>
</head>
<body>
<div class="canvas">

  <section class="card card--front" aria-label="Business card front">
    <div class="brand-dot"></div>
    <div class="brand-name">Ashford Plains deaerator</div>
    <div class="brand-rule"></div>
  </section>

  <section class="card card--back" aria-label="Business card back">
    <div class="brand-row">
      <div class="brand-dot"></div>
      <div class="brand-name">Ashford Plains deaerator</div>
    </div>

    <div class="person">
      <div class="person__name">DANIEL R WHITCOMBE P.E. MBA</div>
      <div class="person__title">PRESIDENT</div>
    </div>

    <div class="divider"></div>

    <div class="contact contact--address">
      <div>4820 W. 98th Street</div>
      <div>Ashford, KS 66000</div>
    </div>
    <div class="contact contact--phone">
      <div><b>P.</b>555-014-2111</div>
      <div><b>F.</b>555-014-2144</div>
    </div>
    <div class="contact contact--online">
      <div><b>E.</b>dwhitcombe@ashfordplains.com</div>
      <div><b>W.</b>www.ashfordplains.com</div>
    </div>
  </section>

</div>
</body>
</html>
```